Kestrel Gardenworks Business Card

An eye catching, yet simple business card that includes;

1. our logo
2. office phone - 5083172946
3. email - kestrelgardenworks@mailbrook.com
4. website - www.kestrelgardenworks.com
5. instagram - @kestrelgardenworksnv

```html
<!DOCTYPE html>
<html lang="en">
<head>
<meta charset="utf-8">
<title>Kestrel Gardenworks Business Card</title>
<link href="https://fonts.googleapis.com/css2?family=Montserrat:wght@600&family=Roboto:wght@400;700;900&display=swap" rel="stylesheet">
<style>
  :root {
    --backdrop: #adadad;
    --card-dark: #1e1e1e;
    --card-light: #ffffff;
    --mark-dark: #0c0c0c;
    --accent: #8b5123;
    --ink: #111111;
    --rule: #9a9a9a;
    --on-dark: #ffffff;
  }
  * { margin: 0; padding: 0; box-sizing: border-box; }
  html, body { width: 1200px; height: 1000px; overflow: hidden; }
  body {
    background: var(--backdrop);
    position: relative;
    font-family: "Roboto", sans-serif;
  }
  .card {
    position: absolute;
    width: 613px;
    height: 352px;
    border-radius: 28px;
    overflow: hidden;
  }
  .card-front { left: 314px; top: 102px; background: var(--card-dark); }
  .card-back { left: 316px; top: 504px; background: var(--card-light); }

  .front-brand {
    position: absolute;
    left: 0; right: 0; top: 155px;
    text-align: center;
    font-family: "Roboto", sans-serif;
    font-weight: 900;
    font-size: 40px;
    color: var(--mark-dark);
    letter-spacing: 0.5px;
  }
  .social-handle {
    position: absolute;
    left: 0; right: 0; top: 302px;
    display: flex; justify-content: center; align-items: center; gap: 7px;
    color: var(--on-dark);
    font-size: 16px;
  }
  .social-handle .dot {
    width: 13px; height: 13px; border: 1.6px solid var(--on-dark); border-radius: 50%;
  }

  .back-brand {
    position: absolute;
    left: 32px; top: 50px;
    font-weight: 900;
    font-size: 22px;
    color: var(--accent);
  }
  .person { position: absolute; left: 31px; top: 208px; }
  .person .name {
    font-family: "Montserrat", sans-serif; font-weight: 600;
    font-size: 17px; color: var(--accent); line-height: 21px;
  }
  .person .title {
    font-family: "Montserrat", sans-serif; font-weight: 600;
    font-size: 16px; color: var(--ink); line-height: 21px;
  }
  .divider {
    position: absolute; left: 31px; top: 256px;
    width: 549px; height: 1px; background: var(--rule);
  }
  .contacts { position: absolute; left: 31px; top: 268px; list-style: none; }
  .contacts li {
    display: flex; align-items: center; gap: 11px;
    font-size: 16px; line-height: 20px; color: var(--ink);
  }
  .contacts svg { width: 15px; height: 15px; fill: var(--accent); flex: none; }
  .address {
    position: absolute; right: 34px; top: 288px;
    text-align: right; font-size: 16px; line-height: 19px; color: var(--ink);
  }
</style>
</head>
<body>
  <section class="card card-front">
    <div class="front-brand">Kestrel Gardenworks</div>
    <div class="social-handle"><span class="dot"></span>kestrelgardenworksnv</div>
  </section>

  <section class="card card-back">
    <div class="back-brand">Kestrel Gardenworks</div>
    <div class="person">
      <p class="name">Name Surname</p>
      <p class="title">Title</p>
    </div>
    <div class="divider"></div>
    <ul class="contacts">
      <li>
        <svg viewBox="0 0 24 24"><path d="M6.6 10.8c1.4 2.8 3.8 5.1 6.6 6.6l2.2-2.2c.3-.3.7-.4 1-.2 1.1.4 2.3.6 3.6.6.6 0 1 .4 1 1V20c0 .6-.4 1-1 1C10.6 21 3 13.4 3 4c0-.6.4-1 1-1h3.5c.6 0 1 .4 1 1 0 1.3.2 2.5.6 3.6.1.3 0 .7-.2 1z"/></svg>
        (508) 317-2946
      </li>
      <li>
        <svg viewBox="0 0 24 24"><path d="M2 5h20v14H2z M4 7v.4l8 5.3 8-5.3V7z" fill-rule="evenodd"/></svg>
        kestrelgardenworks@mailbrook.com
      </li>
      <li>
        <svg viewBox="0 0 24 24"><path d="M12 2a10 10 0 100 20 10 10 0 000-20zm6.9 6h-2.9a15 15 0 00-1.4-3.6A8 8 0 0118.9 8zM12 4c.8 1.2 1.5 2.5 1.9 4h-3.8c.4-1.5 1.1-2.8 1.9-4zM4.3 14a8 8 0 010-4h3.4a16 16 0 000 4zm.8 2h2.9c.3 1.3.8 2.5 1.4 3.6A8 8 0 015.1 16zM8 8H5.1a8 8 0 014.3-3.6C8.8 5.5 8.3 6.7 8 8zm4 12c-.8-1.2-1.5-2.5-1.9-4h3.8c-.4 1.5-1.1 2.8-1.9 4zm2.3-6H9.7a14 14 0 010-4h4.6a14 14 0 010 4zm.3 5.6c.6-1.1 1.1-2.3 1.4-3.6h2.9a8 8 0 01-4.3 3.6zm1.7-5.6a16 16 0 000-4h3.4a8 8 0 010 4z"/></svg>
        www.kestrelgardenworks.com
      </li>
    </ul>
    <p class="address">2260 Linden Hollow Rd, Fallbrook<br>NV, 89431, United States</p>
  </section>
</body>
</html>
```